Agency Growth Partnership Graphic Layout

We need to create a graphic depiction of how our agency helps other advertising agencies make money from the project we start with - and they add on to with elements like PR, ads, and other marketing services that are detailed in the pdf document. The goal is for them to see how the Hollywood project we create is an idea they want to help sell in the clients. The two images we have now are not sexy enough. Originally the idea was to show a seed planted that grows to allow everyone to benefit from the plant. The plant would be the celebrity or TV or Film partnership we create, and then that grows healthier and becomes more robust. However, after we went originally down the path of a plant, we realized it wasn't very sexy looking, and the image our internal team made is not very graphically pleasing or high end enough. We need the graphic to feel like Hollywood, be cool, professional and be attention getting. The graphic can take up an entire PowerPoint page. The second image shows how the other agencies all work with one another (like cogs) off of the central idea that Starline Crafted creates. I like the ideas of growth and plants - but open to other ideas that will show this depiction

Target Market(s)

Media agency executives

Industry/Entity Type

Ad Agency

Font styles to use
Sans Serif

Requirements
Must have
• Everything included (words) in the attached document.
• Our colors are #9b0230 as well as greys, white and black.
Nice to have
• Images that show how the concepts are building blocks, growth, working together
Should not have
• Cartoonish.

```html
<!DOCTYPE html>
<html lang="en">
<head>
<meta charset="UTF-8">
<title>Brand Campaigns – Growing Partnerships Together</title>
<link href="https://fonts.googleapis.com/css2?family=Roboto:wght@400;500;700;900&display=swap" rel="stylesheet">
<style>
  :root {
    --brand: #9b0230;
    --brand-deep: #6e0122;
    --brand-bright: #c0144a;
    --sky: #f5f5f5;
    --grey-900: #141414;
    --grey-800: #232323;
    --grey-700: #2f2f2f;
    --grey-600: #3c3c3c;
    --grey-300: #bdbdbd;
    --ink: #1a1a1a;
    --white: #ffffff;
    --pill-text: #222222;
  }
  * { box-sizing: border-box; margin: 0; padding: 0; }
  html, body { width: 1200px; height: 900px; overflow: hidden; background: var(--sky); }
  body { font-family: "Roboto", sans-serif; }
  .canvas { position: relative; width: 1200px; height: 900px; overflow: hidden; background: var(--sky); }
  .ground { position: absolute; inset: 0; }

  .plant-art {
    position: absolute; left: 430px; top: 6px; width: 350px; height: 300px;
    background: radial-gradient(ellipse 50% 52% at 50% 54%, var(--brand-bright) 0%, var(--brand) 45%, rgba(155,2,48,0.35) 75%, rgba(155,2,48,0) 100%);
  }
  .callout { position: absolute; color: var(--ink); text-align: center; line-height: 1.05; }
  .callout--product { left: 430px; top: 44px; width: 82px; font-size: 11px; font-weight: 500; }
  .callout--celebrity { left: 340px; top: 187px; width: 86px; font-size: 16px; font-weight: 500; }
  .callout--influencer { left: 752px; top: 135px; width: 124px; font-size: 16px; font-weight: 500; }
  .leader { position: absolute; height: 2px; background: var(--ink); }
  .leader::before, .leader::after {
    content: ""; position: absolute; top: -3px; width: 8px; height: 8px; border-radius: 50%; background: var(--ink);
  }
  .leader::before { left: -4px; }
  .leader::after { right: -4px; }

  .banner { position: absolute; left: 164px; top: 328px; width: 858px; height: 60px; background: var(--brand);
    display: flex; align-items: center; justify-content: center; }
  .banner-title { color: var(--white); font-size: 27px; font-weight: 700; letter-spacing: 0.2px;
    text-shadow: 0 2px 2px rgba(0,0,0,.45); }

  .stem { position: absolute; left: 592px; top: 388px; width: 16px; height: 385px; background: var(--brand); border-radius: 4px; }
  .stem-base { position: absolute; left: 552px; top: 770px; width: 96px; height: 6px; background: var(--brand); border-radius: 3px; }
  .twig { position: absolute; height: 7px; background: var(--brand-bright); border-radius: 4px; }

  .pill { position: absolute; height: 35px; background: var(--white); border-radius: 18px;
    display: flex; align-items: center; font-size: 14.5px; color: var(--pill-text); white-space: nowrap; line-height: 1.2; }
  .pill--left { padding-left: 14px; }
  .pill--right { justify-content: flex-start; }
  .pill--tall { height: 46px; border-radius: 23px; }
  .agency { position: absolute; height: 48px; background: var(--brand); border-radius: 9px;
    color: var(--white); font-size: 14.5px; font-weight: 700; text-align: center; line-height: 1.05;
    display: flex; align-items: center; justify-content: center; padding: 0 6px; white-space: nowrap; }

  .footer-line { position: absolute; left: 0; width: 1200px; text-align: center; color: var(--white); }
  .footer-line--title { top: 794px; font-size: 18px; font-weight: 700; }
  .footer-line--sub { top: 816px; font-size: 16.5px; font-weight: 400; }
  .tagline { position: absolute; left: 326px; top: 842px; width: 547px; height: 44px; background: var(--brand);
    border-radius: 22px; display: flex; align-items: center; justify-content: center;
    color: var(--white); font-size: 27px; font-weight: 900; letter-spacing: 1.5px; text-shadow: 0 2px 2px rgba(0,0,0,.4); }
</style>
</head>
<body>
<div class="canvas">
  <svg class="ground" width="1200" height="900" viewBox="0 0 1200 900" aria-hidden="true">
    <rect x="192" y="296" width="832" height="36" rx="10" fill="var(--grey-900)"/>
    <polygon points="120,346 164,346 164,396 120,396 138,371" fill="var(--brand-deep)"/>
    <polygon points="1066,346 1022,346 1022,396 1066,396 1048,371" fill="var(--brand-deep)"/>
    <path d="M0,470 Q0,388 80,388 L1120,388 Q1200,388 1200,470 L1200,900 L0,900 Z" fill="var(--grey-600)"/>
    <path d="M0,620 Q0,558 70,558 L1130,558 Q1200,558 1200,620 L1200,900 L0,900 Z" fill="var(--grey-800)"/>
  </svg>

  <div class="plant-art" role="img" aria-label="Illustration of a growing plant whose leaves hold icons for product placement, celebrity event and influencer endorsement"></div>

  <div class="callout callout--product">Product Placement</div>
  <div class="leader" style="left:471px; top:75px; width:61px;"></div>
  <div class="callout callout--celebrity">Celebrity Event</div>
  <div class="leader" style="left:383px; top:223px; width:71px;"></div>
  <div class="callout callout--influencer">Influencer Endorsement</div>
  <div class="leader" style="left:751px; top:172px; width:63px;"></div>

  <div class="banner"><h1 class="banner-title">Brand Campaigns Can Be Leveraged By All Agency Partners</h1></div>

  <div class="stem"></div>
  <div class="stem-base"></div>

  <div class="twig" style="left:556px; top:428px; width:88px;"></div>
  <div class="twig" style="left:556px; top:481px; width:88px;"></div>
  <div class="twig" style="left:556px; top:534px; width:88px;"></div>
  <div class="twig" style="left:556px; top:587px; width:88px;"></div>
  <div class="twig" style="left:556px; top:639px; width:88px;"></div>
  <div class="twig" style="left:556px; top:692px; width:88px;"></div>
  <div class="twig" style="left:556px; top:745px; width:88px;"></div>

  <div class="pill pill--left" style="left:242px; top:414px; width:300px;">TV, Print, Radio Co-Branded Ads</div>
  <div class="agency" style="left:469px; top:407px; width:89px;">Media<br>Agency</div>

  <div class="pill pill--left" style="left:103px; top:467px; width:320px;">Blogger &amp; Influencer Campaign Extensions</div>
  <div class="agency" style="left:398px; top:460px; width:160px;">Influencer Marketing<br>Agency</div>

  <div class="pill pill--left" style="left:98px; top:520px; width:400px;">Earned Media, Press Stunts, Advetorial, Press Releases</div>
  <div class="agency" style="left:469px; top:513px; width:89px;">PR<br>Agency</div>

  <div class="pill pill--left" style="left:48px; top:573px; width:370px;">Digital Content, Contests, Landing Pages, Mocrosite</div>
  <div class="agency" style="left:398px; top:566px; width:160px;">Inbound Marketing<br>Agency</div>

  <div class="pill pill--left" style="left:94px; top:625px; width:400px;">Coupons, Merchandising Displays, Packaging, Contests</div>
  <div class="agency" style="left:469px; top:618px; width:89px;">Promotion<br>Agency</div>

  <div class="pill pill--left" style="left:169px; top:678px; width:300px;">Targeted Content Partnership Extensions</div>
  <div class="agency" style="left:453px; top:671px; width:105px;">Multicultural<br>Agency</div>

  <div class="pill pill--left" style="left:185px; top:731px; width:290px;">Social Post, Contests, Custom Content</div>
  <div class="agency" style="left:453px; top:724px; width:105px;">Social Media<br>Agency</div>

  <div class="pill pill--right" style="left:700px; top:414px; width:448px; padding-left:42px;">Graphic Design, Creative Copy Elements for Campaign Design</div>
  <div class="agency" style="left:643px; top:407px; width:89px;">Creative<br>Agency</div>

  <div class="pill pill--right pill--tall" style="left:700px; top:461px; width:438px; padding-left:42px;">Digital Ads, SEO, Search, Website or Microsite Build, PPC,<br>Marketing Automation, Email Campaign, CTA, Sweepstakes</div>
  <div class="agency" style="left:643px; top:460px; width:89px;">Interactive<br>Agency</div>

  <div class="pill pill--right pill--tall" style="left:710px; top:514px; width:392px; padding-left:41px;">Content, Contests, Giveaways, Talent Appearances,<br>for Onsite Trade Show</div>
  <div class="agency" style="left:643px; top:513px; width:97px;">Trade Show<br>Marketing</div>

  <div class="pill pill--right pill--tall" style="left:780px; top:567px; width:373px; padding-left:37px;">Red Carpet Events, Premiere Parties, Screenings,<br>Talent Appearances</div>
  <div class="agency" style="left:643px; top:566px; width:163px;">Experiential &amp; Guerilla<br>Marketing Agency</div>

  <div class="pill pill--right" style="left:740px; top:625px; width:164px; padding-left:44px;">Recall Tracking</div>
  <div class="agency" style="left:643px; top:618px; width:129px;">Market Research<br>Agency</div>

  <div class="pill pill--right" style="left:740px; top:678px; width:192px; padding-left:44px;">Content, Flash Sales</div>
  <div class="agency" style="left:643px; top:671px; width:129px;">Direct Marketing<br>Agency</div>

  <div class="pill pill--right" style="left:740px; top:731px; width:199px; padding-left:44px;">OHH Co-Branded Ads</div>
  <div class="agency" style="left:643px; top:724px; width:129px;">OOH Marketing<br>Agency</div>

  <p class="footer-line footer-line--title">Starline Crafted Influencer &amp; Entertaiment Marketing Campaigns</p>
  <p class="footer-line footer-line--sub">Product Placement&nbsp; |&nbsp; Influencer Endorsement&nbsp; |&nbsp; Celebrity Event Activation</p>
  <div class="tagline">GROWING PARTNERSHIPS TOGETHER</div>
</div>
</body>
</html>
```